Corwen Physical Therapy Website

I would need a clean modern website built to showcase my Physical therapy brand and services. I would need a simple but descriptive website that can ultimately connect my patients to my electronic medical portal so they may book an appointment..

```html
<!DOCTYPE html>
<html lang="en">
<head>
<meta charset="utf-8">
<title>Corwen Physical Therapy &amp; Wellness</title>
<link href="https://fonts.googleapis.com/css2?family=Lexend:wght@300;400;500;600&family=Lato:ital,wght@0,400;0,700;1,400&display=swap" rel="stylesheet">
<style>
:root{
  --teal:#17857f;
  --teal-soft:#3d9a94;
  --teal-tint:#d3ebe8;
  --green:#7cc35a;
  --blue:#3f56a3;
  --ink:#222;
  --muted:#555;
  --line:#e3e3e3;
  --white:#fff;
}
*{margin:0;padding:0;box-sizing:border-box}
html,body{width:1200px;height:5026px;overflow:hidden;background:var(--white)}
body{font-family:"Lato",sans-serif;color:var(--ink);position:relative}
.abs{position:absolute}
section,header,footer{position:absolute;left:0;width:1200px}
h1,h2,h3,h4{font-family:"Lexend",sans-serif;font-weight:300}
.badge{position:absolute;height:35px;border-radius:18px;font:600 11px "Lexend",sans-serif;letter-spacing:1.5px;display:flex;align-items:center;justify-content:center;text-transform:uppercase}
.badge.light{background:var(--teal-tint);color:var(--teal)}
.badge.dark{background:var(--teal-soft);color:var(--white)}
.badge.onblue{background:#5a70b7;color:var(--white)}
.btn{position:absolute;background:var(--green);color:var(--white);font:600 13px "Lexend",sans-serif;border-radius:24px;display:flex;align-items:center;justify-content:center}
.photo{position:absolute}
.read-more{font:600 11px "Lexend",sans-serif;color:var(--green);display:flex;align-items:center;gap:5px}
.read-more i{width:11px;height:11px;border-radius:50%;background:var(--green);display:inline-block;position:relative}
.read-more i::after{content:"";position:absolute;left:3px;top:3px;border-left:5px solid var(--white);border-top:2.5px solid transparent;border-bottom:2.5px solid transparent}

/* top bar */
.topbar{top:0;height:43px;background:var(--teal);color:var(--white);font-size:12px}
.topbar .contact{position:absolute;top:14px;display:flex;align-items:center;gap:8px}
.topbar .social{position:absolute;right:70px;top:13px;display:flex;gap:22px}
.topbar .social span{width:16px;height:16px;border-radius:50%;border:2px solid var(--white)}

/* hero */
.hero{top:43px;height:601px}
.brand{position:absolute;display:flex;align-items:center;gap:8px;font:600 30px "Lexend",sans-serif;color:var(--teal)}
.brand span{width:26px;height:26px;border-radius:50%;background:var(--green)}
.nav{position:absolute;top:35px;left:451px;display:flex;gap:50px;font-size:14px;color:var(--ink)}
.nav .active{color:var(--teal)}
.hero-photo{left:546px;top:0;width:654px;height:600px;background:radial-gradient(ellipse at 60% 40%,#d8b7a4 0%,#c99f8e 25%,#e9ecf3 55%,#fff 78%)}
.tagline{left:74px;top:200px;font:italic 400 20px "Lato",sans-serif;color:var(--teal);display:flex;align-items:center;gap:6px}
.tagline::after{content:"";width:112px;height:1px;background:#9bbcba;margin-top:6px}
.hero-title{left:76px;top:242px;font-size:48px;line-height:60px;color:var(--ink)}
.hero-title b{font-weight:600;display:block}
.scroll{left:64px;top:520px;font-size:11px;letter-spacing:1px;transform:rotate(-90deg);transform-origin:left top;top:620px;color:#333}

/* about */
.about{top:644px;height:653px}
.arch-line{position:absolute;border:2px solid var(--green);border-bottom:none;border-radius:215px 215px 0 0}
.about-photo{left:82px;top:54px;width:429px;height:531px;border-radius:215px 215px 0 0;background:linear-gradient(160deg,#d7dde3,#b9c2cc 50%,#2e4fb0 88%)}
.section-title{position:absolute;font-size:38px;line-height:48px}
.body-text{position:absolute;font-size:13.5px;line-height:24px;color:var(--muted)}

/* services */
.services{top:1297px;height:800px;color:var(--white)}
.services svg.band{position:absolute;left:0;top:0}
.service{position:absolute;width:320px;height:110px}
.service .icon{position:absolute;left:0;top:0;width:78px;height:78px;border-radius:22px 22px 40px 22px;background:var(--green);display:flex;align-items:center;justify-content:center}
.service h3{position:absolute;left:90px;top:-6px;font-size:22px;font-weight:300}
.service p{position:absolute;left:90px;top:26px;width:220px;font-size:13px;line-height:21px}
.service .read-more{position:absolute;left:90px;top:80px}
.services-photo{left:734px;top:192px;width:392px;height:482px;border-radius:196px 196px 0 0;background:linear-gradient(170deg,#e8e3dd,#cfd6dd 45%,#f2f2f2 75%,#9fc6e6)}

/* why */
.why{top:2088px;height:752px}
.feature{position:absolute;width:277px;height:142px;border-radius:22px;background:var(--white);box-shadow:0 6px 18px rgba(0,0,0,.12);border-left:3px solid #e8e8ee}
.feature .ficon{position:absolute;left:-3px;top:0;width:58px;height:58px;border-radius:22px 0 22px 0;background:var(--blue);display:flex;align-items:center;justify-content:center}
.feature h4{position:absolute;left:78px;top:30px;font-size:15px;font-weight:400;color:var(--ink)}
.feature p{position:absolute;left:78px;top:56px;width:180px;font-size:13px;line-height:21px;color:var(--muted)}
.appointment{left:700px;top:85px;width:420px;height:553px;background:var(--blue);border-radius:6px}
.appointment h3{position:absolute;left:26px;top:34px;font-size:30px;color:var(--white)}
.field{position:absolute;height:43px;background:var(--white);font-size:13px;color:#333;display:flex;align-items:center;padding-left:12px}
.field .caret{position:absolute;right:0;top:0;width:40px;height:43px;border-left:1px solid #ddd;display:flex;align-items:center;justify-content:center}
.field .caret::after{content:"";border-top:5px solid #888;border-left:5px solid transparent;border-right:5px solid transparent}

/* team */
.team{top:2840px;height:680px;color:var(--white)}
.team svg.band{position:absolute;left:0;top:0}
.member{position:absolute;top:194px;width:234px;text-align:center}
.member .portrait{width:234px;height:254px;border-radius:40px 40px 40px 40px;border-bottom:3px solid var(--white)}
.member h4{margin-top:18px;font:600 19px "Lato",sans-serif}
.member em{display:block;font-size:11px;margin-top:4px}
.arrow{position:absolute;width:36px;height:36px;border-radius:50%;display:flex;align-items:center;justify-content:center}
.arrow::after{content:"";width:9px;height:9px;border-top:2px solid var(--white);border-right:2px solid var(--white)}
.arrow.next::after{transform:rotate(45deg);margin-left:-4px}
.arrow.prev::after{transform:rotate(-135deg);margin-left:4px}

/* testimonials */
.testimonials{top:3502px;height:420px}
.quote{position:absolute;top:140px;width:320px}
.quote .mark{position:absolute;left:0;top:0;font:400 46px/1 "Lexend",sans-serif;color:var(--green)}
.quote p{position:absolute;left:37px;top:10px;width:280px;font-style:italic;font-size:14px;line-height:24px;color:#444}
.quote .who{position:absolute;left:0;top:155px;display:flex;align-items:center;gap:12px}
.quote .avatar{width:50px;height:50px;border-radius:50%;background:linear-gradient(135deg,#c9c2bb,#6f6a66)}
.quote .who b{display:block;font:600 14px "Lexend",sans-serif;color:var(--teal)}
.quote .who em{font-size:12px;color:#888}
.dots{position:absolute;left:563px;top:390px;display:flex;gap:19px}
.dots span{width:10px;height:10px;background:#d9e4e3}
.dots span.on{background:var(--teal)}

/* blog */
.blog{top:3922px;height:730px;color:var(--white)}
.blog svg.band{position:absolute;left:0;top:0}
.post{position:absolute;top:177px;width:337px;height:404px;background:var(--white);border-radius:4px;overflow:hidden;color:var(--ink)}
.post .thumb{height:213px}
.post .date{position:absolute;left:22px;top:235px;font-size:11px;color:#555;display:flex;gap:6px;align-items:center}
.post .date i{width:9px;height:9px;background:var(--teal)}
.post h4{position:absolute;left:22px;top:250px;font-size:19px;font-weight:300}
.post p{position:absolute;left:22px;top:292px;width:295px;font-size:13px;line-height:21px;color:var(--muted)}
.post .read-more{position:absolute;left:22px;top:372px}

/* footer */
.site-footer{top:4643px;height:319px;font-size:12px;color:#444}
.site-footer h5{position:absolute;top:70px;font:500 14px "Lexend",sans-serif;color:var(--ink)}
.links{position:absolute;top:106px;list-style:none;line-height:38px}
.hours{position:absolute;left:706px;top:98px;width:420px;border-collapse:collapse}
.hours td{height:43px;border-bottom:1px solid var(--line);font-size:12px;padding:0}
.copyright{top:4962px;height:64px;background:var(--teal);color:var(--white);font-size:12px}
.copyright .left{position:absolute;left:70px;top:26px}
.copyright .right{position:absolute;right:70px;top:26px;display:flex;gap:14px}
</style>
</head>
<body>

<div class="abs topbar" style="left:0;width:1200px">
  <div class="contact" style="left:70px">
    <svg width="13" height="10" viewBox="0 0 13 10"><rect x="0.5" y="0.5" width="12" height="9" fill="none" stroke="#fff"/><path d="M1 1l5.5 4.5L12 1" fill="none" stroke="#fff"/></svg>
    info@corwenphysio.com
  </div>
  <div class="contact" style="left:330px">
    <svg width="11" height="11" viewBox="0 0 12 12"><path d="M2 1l2 0 1 3-1.5 1a7 7 0 003.5 3.5L8 7l3 1v2c0 .6-.4 1-1 1A10 10 0 011 2c0-.6.4-1 1-1z" fill="#fff"/></svg>
    +01 555 010 2040
  </div>
  <div class="social"><span></span><span></span><span></span><span></span></div>
</div>

<header class="hero">
  <div class="photo hero-photo" role="img" aria-label="Therapist massaging the neck and shoulder of a smiling patient"></div>
  <div class="brand" style="left:72px;top:60px"><span></span>CORWEN</div>
  <nav class="nav"><span class="active">Home</span><span>About Us</span><span>Services</span><span>Blog</span><span>Contact Us</span></nav>
  <div class="btn" style="left:954px;top:17px;width:174px;height:47px">Book Appointment</div>
  <div class="abs tagline">Get your Lifestyle Back</div>
  <h1 class="abs hero-title">We Offer Highly<b>Specialized Therapy</b></h1>
  <div class="btn" style="left:72px;top:386px;width:150px;height:45px">Know More</div>
  <div class="abs scroll">SCROLL DOWN</div>
</header>

<section class="about">
  <div class="arch-line" style="left:101px;top:46px;width:426px;height:529px;border-right:2px solid var(--green);border-left:2px solid var(--green)"></div>
  <div class="photo about-photo" role="img" aria-label="Physiotherapist treating a patient lying on a treatment table"></div>
  <div class="badge light" style="left:611px;top:115px;width:119px">About Us</div>
  <h2 class="section-title" style="left:611px;top:164px">Corwen Physical Therapy<br>&amp; Wellness</h2>
  <p class="body-text" style="left:611px;top:266px;width:520px">Lorem ipsum dolor sit amet, consectetur adipiscing elit, sed do eiusmod tempor incididunt ut labore et dolore magna aliqua. Quis ipsum suspendisse ultrices gravida. Risus commodo viverra maecenas accumsan lacus vel facilisis. Vestibulum blandit risus ac commodo ornare. Ut et bibendum purus, a facilisis lectus. Nulla varius, dolor vitae varius tempor, nibh tortor vivrra ex, et faucibus elit ligula vel arcu. Sed laoreet odio ac ipsum vulputate accusan. Duis placerat sapien dapibus malesuada commodo.</p>
  <div class="btn" style="left:611px;top:464px;width:152px;height:47px">Read More</div>
</section>

<section class="services">
  <svg class="band" width="1200" height="800" viewBox="0 0 1200 800"><path d="M0 59Q600-60 1200 49V791Q600 675 0 796Z" fill="#17857f"/></svg>
  <div class="badge dark" style="left:70px;top:90px;width:119px">Services</div>
  <h2 class="section-title" style="left:70px;top:140px;color:#fff">Physical Therapy<br>Services</h2>

  <div class="service" style="left:70px;top:273px"><div class="icon"><svg width="36" height="36" viewBox="0 0 36 36" fill="none" stroke="#fff" stroke-width="2"><circle cx="18" cy="8" r="4"/><path d="M18 12v12M10 18h16M12 32l6-8 6 8"/></svg></div><h3>Physical Therapy</h3><p>Sed laoreet odio ac ip vulputate accusan. Duis placerat sapien</p><span class="read-more">Read More <i></i></span></div>
  <div class="service" style="left:406px;top:273px"><div class="icon"><svg width="36" height="36" viewBox="0 0 36 36" fill="none" stroke="#fff" stroke-width="2"><circle cx="12" cy="12" r="4"/><path d="M4 26h28M8 26l4-10 8 4M26 26v6M8 26v6"/></svg></div><h3>Massage Therapy</h3><p>Sed laoreet odio ac ip vulputate accusan. Duis placerat sapien</p><span class="read-more">Read More <i></i></span></div>
  <div class="service" style="left:70px;top:418px"><div class="icon"><svg width="36" height="36" viewBox="0 0 36 36" fill="none" stroke="#fff" stroke-width="2"><path d="M8 10h14a6 6 0 010 12H14v8M8 16h10"/></svg></div><h3>Chirpractic Thrapy</h3><p>Sed laoreet odio ac ip vulputate accusan. Duis placerat sapien</p><span class="read-more">Read More <i></i></span></div>
  <div class="service" style="left:406px;top:418px"><div class="icon"><svg width="36" height="36" viewBox="0 0 36 36" fill="none" stroke="#fff" stroke-width="2"><circle cx="16" cy="7" r="3"/><path d="M16 11v10h8l3 8M16 16h-4"/><circle cx="14" cy="25" r="7"/></svg></div><h3>Work Injuries</h3><p>Sed laoreet odio ac ip vulputate accusan. Duis placerat sapien</p><span class="read-more">Read More <i></i></span></div>
  <div class="service" style="left:70px;top:568px"><div class="icon"><svg width="36" height="36" viewBox="0 0 36 36" fill="none" stroke="#fff" stroke-width="2"><circle cx="22" cy="7" r="3"/><path d="M10 14l8-3 4 8-6 6M22 19l6 4M16 25l-6 7"/></svg></div><h3>Sport Injuries</h3><p>Sed laoreet odio ac ip vulputate accusan. Duis placerat sapien</p><span class="read-more">Read More <i></i></span></div>
  <div class="service" style="left:406px;top:568px"><div class="icon"><svg width="36" height="36" viewBox="0 0 36 36" fill="none" stroke="#fff" stroke-width="2"><path d="M4 24h28M6 24v6M30 24v6M8 24v-6h20v6"/><circle cx="12" cy="14" r="3"/></svg></div><h3>Other Therapy</h3><p>Sed laoreet odio ac ip vulputate accusan. Duis placerat sapien</p><span class="read-more">Read More <i></i></span></div>

  <div class="arch-line" style="left:722px;top:176px;width:381px;height:478px;border-left:2px solid var(--green);border-right:2px solid var(--green);border-radius:190px 190px 0 0"></div>
  <div class="photo services-photo" role="img" aria-label="Masked clinician stretching the arm of a patient"></div>
</section>

<section class="why">
  <h2 class="section-title" style="left:70px;top:118px">Why Choose Us</h2>
  <p class="body-text" style="left:70px;top:172px;width:520px">Risus commodo viverra maecenas accumsan lacus vel facilisis. Vestibulum blandit risus ac commodo ornare. Ut et bibendum purus, a facilisis lectus. Nulla varius, dolor vitae varius tempor, nibh tortor vivrra ex, et faucibus elit ligula vel arcu.</p>

  <div class="feature" style="left:70px;top:277px"><div class="ficon"><svg width="26" height="26" viewBox="0 0 26 26" fill="#fff"><circle cx="13" cy="7" r="4"/><rect x="5" y="14" width="16" height="8" rx="3"/></svg></div><h4>Personalized Treatment</h4><p>A facilisis lectus. Nulla varius, dolor vitae varius tempor</p></div>
  <div class="feature" style="left:373px;top:277px"><div class="ficon"><svg width="24" height="26" viewBox="0 0 24 26" fill="none" stroke="#fff" stroke-width="2"><rect x="3" y="3" width="18" height="20" rx="2"/><path d="M8 10h8M8 15h8"/></svg></div><h4>Experience Staff</h4><p>A facilisis lectus. Nulla varius, dolor vitae varius tempor</p></div>
  <div class="feature" style="left:70px;top:452px"><div class="ficon"><svg width="26" height="26" viewBox="0 0 26 26" fill="none" stroke="#fff" stroke-width="2"><rect x="3" y="6" width="20" height="17"/><path d="M13 10v8M9 14h8"/></svg></div><h4>Comfortable Clinic</h4><p>A facilisis lectus. Nulla varius, dolor vitae varius tempor</p></div>
  <div class="feature" style="left:373px;top:452px"><div class="ficon"><svg width="26" height="26" viewBox="0 0 26 26" fill="none" stroke="#fff" stroke-width="2"><circle cx="12" cy="14" r="9"/><circle cx="12" cy="14" r="4"/><path d="M12 14L22 4"/></svg></div><h4>Therapy Goals</h4><p>A facilisis lectus. Nulla varius, dolor vitae varius tempor</p></div>

  <form class="abs appointment">
    <h3>Fix an Appointment</h3>
    <div class="field" style="left:24px;top:90px;width:374px">Name</div>
    <div class="field" style="left:24px;top:147px;width:374px">Phone</div>
    <div class="field" style="left:24px;top:207px;width:374px">Type Of Service<span class="caret"></span></div>
    <div class="field" style="left:24px;top:268px;width:374px">Staff<span class="caret"></span></div>
    <div class="field" style="left:24px;top:326px;width:374px">MM/DD/YYYY<span class="caret" style="border:none"><svg width="12" height="12" viewBox="0 0 12 12"><rect x="1" y="2" width="10" height="9" fill="none" stroke="#888"/><path d="M1 5h10" stroke="#888"/></svg></span></div>
    <div class="field" style="left:24px;top:393px;width:179px">From<span class="caret"></span></div>
    <div class="field" style="left:219px;top:393px;width:179px">To<span class="caret"></span></div>
    <div class="btn" style="left:24px;top:455px;width:374px;height:49px;border-radius:25px">Check Availability</div>
  </form>
</section>

<section class="team">
  <svg class="band" width="1200" height="680" viewBox="0 0 1200 680"><path d="M0 40Q600-40 1200 48V620Q600 700 0 662Z" fill="#3f56a3"/></svg>
  <div class="badge onblue" style="left:540px;top:55px;width:120px">Team</div>
  <h2 class="section-title" style="left:0;width:1200px;top:104px;text-align:center;color:#fff">Meet the Team</h2>
  <div class="member" style="left:70px"><div class="portrait" role="img" aria-label="Portrait of a smiling bearded therapist" style="background:linear-gradient(160deg,#dbc9b3,#a8866c)"></div><h4>Martin Hale</h4><em>Physical Therapist</em></div>
  <div class="member" style="left:338px"><div class="portrait" role="img" aria-label="Portrait of a therapist in light blue scrubs" style="background:linear-gradient(160deg,#e6e6e6,#9ec4d8)"></div><h4>Elena Brooks</h4><em>Massage Therapist</em></div>
  <div class="member" style="left:605px"><div class="portrait" role="img" aria-label="Portrait of a smiling chiropractor" style="background:linear-gradient(160deg,#eeeeee,#5a5a5a)"></div><h4>Daniel Reyes</h4><em>Chiropractor</em></div>
  <div class="member" style="left:872px"><div class="portrait" role="img" aria-label="Portrait of a therapist in front of bookshelves" style="background:linear-gradient(160deg,#a77b5e,#e0c7b5)"></div><h4>Clara Whitfield</h4><em>Physical Therapist</em></div>
  <div class="arrow prev" style="left:52px;top:310px;background:#6d7fb9"></div>
  <div class="arrow next" style="left:1100px;top:310px;background:var(--green)"></div>
</section>

<section class="testimonials">
  <div class="badge light" style="left:529px;top:25px;width:142px">Testimonial</div>
  <h2 class="section-title" style="left:0;width:1200px;top:58px;text-align:center">What Our Clients Say</h2>
  <div class="quote" style="left:70px"><span class="mark">&ldquo;</span><p>Risus commodo viverra manas accumsan las vel facilisis. Vestilum blandit risus ac commodo ornare. Ut et bibendum purus, a facilisis lectus. Nulla varius, dolor vitae varius tempor.</p><div class="who"><span class="avatar" role="img" aria-label="Client photo"></span><div><b>Lorem ipsum</b><em>Simply Dummy</em></div></div></div>
  <div class="quote" style="left:435px"><span class="mark">&ldquo;</span><p>Risus commodo viverra manas accumsan las vel facilisis. Vestilum blandit risus ac commodo ornare. Ut et bibendum purus, a facilisis lectus. Nulla varius, dolor vitae varius tempor.</p><div class="who"><span class="avatar" role="img" aria-label="Client photo"></span><div><b>Lorem ipsum</b><em>Simply Dummy</em></div></div></div>
  <div class="quote" style="left:802px"><span class="mark">&ldquo;</span><p>Risus commodo viverra manas accumsan las vel facilisis. Vestibulum blandit risus ac commodo ornare. Ut et bibendum purus, a facilisis lectus. Nulla varius, dolor vitae varius tempor.</p><div class="who"><span class="avatar" role="img" aria-label="Client photo"></span><div><b>Lorem ipsum</b><em>Simply Dummy</em></div></div></div>
  <div class="dots"><span class="on"></span><span></span><span></span></div>
</section>

<section class="blog">
  <svg class="band" width="1200" height="730" viewBox="0 0 1200 730"><path d="M0 60Q600-40 1200 40V722Q600 640 0 730Z" fill="#17857f"/></svg>
  <div class="badge dark" style="left:540px;top:76px;width:120px">Blog</div>
  <h2 class="section-title" style="left:0;width:1200px;top:122px;text-align:center;color:#fff">Blog Posts</h2>
  <article class="post" style="left:72px"><div class="thumb" role="img" aria-label="Patient wearing a neck brace beside a clinician" style="background:linear-gradient(160deg,#ece8e4,#bfb4ab)"></div><span class="date"><i></i>Aug 12, 2021</span><h4>Vestibulum blandit risus</h4><p>Ut hendrerit mattis ante a egestas. Ut eget mi mauris. Phasellus metus ipsum, semper et laoreet ut, ullamcorper eget libero.</p><span class="read-more">Read More <i></i></span></article>
  <article class="post" style="left:427px"><div class="thumb" role="img" aria-label="Therapist examining a patient's leg" style="background:linear-gradient(160deg,#f0eded,#c6c9cf)"></div><span class="date"><i></i>Aug 12, 2021</span><h4>Vestibulum blandit risus</h4><p>Ut hendrerit mattis ante a egestas. Ut eget mi mauris. Phasellus metus ipsum, semper et laoreet ut, ullamcorper eget libero.</p><span class="read-more">Read More <i></i></span></article>
  <article class="post" style="left:782px"><div class="thumb" role="img" aria-label="Gloved hands holding a patient's knee" style="background:linear-gradient(160deg,#f2f2f2,#9fb5d3)"></div><span class="date"><i></i>Aug 12, 2021</span><h4>Vestibulum blandit risus</h4><p>Ut hendrerit mattis ante a egestas. Ut eget mi mauris. Phasellus metus ipsum, semper et laoreet ut, ullamcorper eget libero.</p><span class="read-more">Read More <i></i></span></article>
  <div class="arrow prev" style="left:52px;top:343px;background:#4a9e98"></div>
  <div class="arrow next" style="left:1100px;top:343px;background:var(--green)"></div>
</section>

<footer class="site-footer">
  <div class="brand" style="left:72px;top:52px"><span></span>CORWEN</div>
  <p class="abs" style="left:72px;top:166px;line-height:24px">12 Harbour Lane, Rosewood<br>Sydney, Australia<br>info@corwenphysio.com<br>+01 555 010 2040</p>
  <h5 style="left:336px">Quick Links</h5>
  <ul class="links" style="left:336px"><li>Home</li><li>About Us</li><li>Services</li><li>Blog</li><li>Contact Us</li></ul>
  <h5 style="left:521px">Services</h5>
  <ul class="links" style="left:521px"><li>Phsical Therapy</li><li>Massage Therapy</li><li>Chirpractic thrapy</li><li>Work Injuries</li><li>Sport Injuries</li></ul>
  <h5 style="left:706px">Working Hours</h5>
  <table class="hours">
    <tr><td style="width:123px">Monday</td><td style="width:105px">7am &ndash; 6pm</td><td style="width:129px">Thursday</td><td>7am &ndash; 6pm</td></tr>
    <tr><td>Tuesday</td><td>7am &ndash; 6pm</td><td>Friday</td><td>7am &ndash; 6pm</td></tr>
    <tr><td>Wednesday</td><td>7am &ndash; 6pm</td><td>Sat &ndash; sun</td><td>Closed</td></tr>
  </table>
</footer>

<div class="abs copyright" style="left:0;width:1200px">
  <span class="left">&copy; 2021 <b>Corwen Physical Therapy &amp; Wellness.</b> All right reserved</span>
  <span class="right"><span>Facenote</span>&bull;<span>Chirper</span>&bull;<span>Viewtube</span>&bull;<span>Snapgram</span></span>
</div>

</body>
</html>
```